Advert for Services that we offer

Brenwick Torque Ltd need an design to represent what we do in a modern way by showing an image with a brief description and the use of corporate logo the information we will proved vie a doc file and this is to be presented in a modern way. This design will be for print & web. we have done our own design and its not great i have put this in the file repository

Target Market(s)

Motor trade

Font styles to use
Sans Serif

Colors

Designer to choose colors to be used in the design.

Requirements
Must have
• Company colour scheme as per logo within the files uploaded.
• and a small boarder to isolate it from the rest of the articles.
Nice to have
• Modern font
Should not have
• Old style font

```html
<!DOCTYPE html>
<html lang="en">
<head>
<meta charset="utf-8">
<title>Brenwick Torque Ltd – Product Testing &amp; Analysis</title>
<link href="https://fonts.googleapis.com/css2?family=Roboto+Condensed:wght@500;700&family=Montserrat:wght@500;600&display=swap" rel="stylesheet">
<style>
  :root {
    --page-grey: #d6d6d6;
    --brand-blue: #1f6fbf;
    --brand-navy: #1b2a44;
    --item-tint: #e9f0f8;
    --paper: #ffffff;
    --badge-red: #d7141e;
    --rule-grey: #9aa3ad;
  }
  * { box-sizing: border-box; margin: 0; padding: 0; }
  html, body { width: 1200px; height: 826px; overflow: hidden; }
  body { background: var(--page-grey); position: relative; font-family: "Roboto Condensed", Arial, sans-serif; }

  .advert {
    position: absolute; left: 120px; top: 93px; width: 960px; height: 621px;
    background: var(--paper); overflow: hidden;
    box-shadow: 0 3px 10px rgba(0,0,0,0.25);
  }

  .brand { position: absolute; left: 108px; top: 58px; width: 290px; text-align: center; }
  .brand-mark { width: 34px; height: 34px; background: var(--brand-blue); margin: 0 auto 14px; }
  .brand-name {
    font-family: "Montserrat", Arial, sans-serif; font-weight: 600;
    font-size: 27px; letter-spacing: 1px; color: var(--brand-blue); white-space: nowrap;
  }
  .brand-suffix {
    display: flex; align-items: center; gap: 10px; margin-top: 4px;
    font-family: "Montserrat", Arial, sans-serif; font-weight: 600;
    font-size: 15px; letter-spacing: 5px; color: var(--brand-blue);
  }
  .brand-suffix::before, .brand-suffix::after { content: ""; flex: 1; height: 2px; background: var(--brand-blue); }

  .headline {
    position: absolute; left: 54px; top: 178px; width: 416px; height: 62px;
    background: var(--brand-blue); border-radius: 6px; color: var(--paper);
    font-weight: 700; font-size: 31px; display: flex; align-items: center; justify-content: center;
  }

  .service-list { position: absolute; left: 72px; top: 267px; list-style: none; }
  .service-list li {
    display: table; height: 45px; margin-bottom: 7.5px; padding: 0 16px 0 14px;
    background: var(--item-tint); border-left: 4px solid var(--brand-blue);
    color: var(--brand-navy); font-weight: 700; font-size: 25px; line-height: 45px;
  }

  .web-band {
    position: absolute; left: 0; bottom: 0; width: 436px; height: 57px;
    background: var(--brand-blue); color: var(--paper);
    font-family: "Montserrat", Arial, sans-serif; font-weight: 500; font-size: 21px;
    letter-spacing: 2.5px; display: flex; align-items: center; padding-left: 68px;
  }

  .workshop-photo {
    position: absolute; left: 436px; top: 0; width: 524px; height: 621px;
    background: linear-gradient(160deg, #eef0f2 0%, #c9ccd0 35%, #4a4d55 60%, #8a8c90 100%);
  }

  .partner-corner { position: absolute; right: 0; bottom: 0; width: 263px; height: 174px; }
  .partner-badge { position: absolute; left: 798px; top: 537px; width: 129px; height: 40px; background: var(--badge-red); }
  .partner-caption {
    position: absolute; left: 780px; top: 582px; width: 165px; text-align: center;
    color: var(--paper); font-family: "Montserrat", Arial, sans-serif; font-size: 12.5px; font-weight: 500;
  }
</style>
</head>
<body>
  <main class="advert">
    <div class="brand">
      <div class="brand-mark"></div>
      <div class="brand-name">BRENWICK TORQUE</div>
      <div class="brand-suffix">LTD</div>
    </div>

    <h1 class="headline">Product Testing &amp; Analysis</h1>

    <ul class="service-list">
      <li>Metallurgical testing</li>
      <li>Bearing pre-load testing</li>
      <li>Bore measurement</li>
      <li>New product evaluation</li>
      <li>Product analysis &amp; report</li>
    </ul>

    <div class="web-band">www.brenwick-torque.co.uk</div>

    <div class="workshop-photo" role="img" aria-label="Technician in dark overalls tapping a wheel hub with a hammer on a workshop test bench"></div>

    <svg class="partner-corner" viewBox="0 0 263 174" aria-hidden="true">
      <polygon points="0,174 263,0 263,174" fill="var(--brand-blue)"/>
    </svg>
    <div class="partner-badge" role="img" aria-label="Partner badge"></div>
    <div class="partner-caption">Authorised Distributor</div>
  </main>
</body>
</html>
```